Bref créative
RL Advisory
I need double sided standard sized Business Card [3.5" x 2"]
Use same font as in logo...also can mix it up with complimentary font
Professional
Romy Lindqvist, MSc, PCC
Harlow Springs, OR
rl@romylindqvist-demo.com
www.romylindqvist-demo.com
please add twitter account underneath email address
Twitter: @RLpathways
Symbol only in the middle of the back of card.
with website address noted again underneath the symbol (www.romylindqvist-demo.com)

```html
<!DOCTYPE html>
<html lang="en">
<head>
<meta charset="utf-8">
<title>RL Advisory — Business Card Concepts</title>
<link rel="stylesheet" href="https://fonts.googleapis.com/css2?family=Source+Sans+3:wght@400;600;700&display=swap">
<style>
  :root {
    --maroon: #6d0b12;
    --maroon-text: #7d1219;
    --ink: #1d1d1d;
    --white: #ffffff;
    --paper-edge: #c9c9c9;
    --grey-light: #f1f1f1;
    --grey-dark: #a9a9a9;
    --sans: "Source Sans 3", "Myriad Pro", Arial, sans-serif;
  }
  * { box-sizing: border-box; margin: 0; padding: 0; }
  html, body { width: 1200px; height: 713px; overflow: hidden; background: var(--white); }
  .sheet { position: relative; width: 1200px; height: 713px; font-family: var(--sans); }

  .card {
    position: absolute;
    width: 552px; height: 312px;
    border: 1px solid var(--paper-edge);
    overflow: hidden;
    background: var(--white);
  }
  .card--front { left: 24px; top: 24px; }
  .card--back-white { left: 619px; top: 24px; }
  .card--back-maroon { left: 24px; top: 372px; background: var(--maroon); border-color: var(--maroon); }
  .card--back-grey { left: 619px; top: 372px; background: radial-gradient(ellipse at 50% 45%, var(--grey-light) 0%, #d6d6d6 55%, var(--grey-dark) 100%); }

  .wave { position: absolute; inset: 0; width: 100%; height: 100%; }

  .brand { position: absolute; display: flex; flex-direction: column; align-items: flex-start; }
  .brand__row { display: flex; align-items: center; gap: 10px; }
  .brand__dot { width: 26px; height: 26px; border-radius: 50%; background: var(--maroon); flex: none; }
  .brand__name { font-weight: 700; font-size: 34px; line-height: 1; color: var(--ink); letter-spacing: -0.5px; white-space: nowrap; }
  .brand__tagline { font-weight: 600; font-size: 12px; color: var(--ink); margin-left: 36px; margin-top: 3px; white-space: nowrap; }

  .brand--front { left: 22px; top: 90px; }
  .brand--front .brand__name { font-size: 30px; }

  .brand--centered { left: 50%; top: 122px; transform: translateX(-50%); }
  .card--back-maroon .brand__name,
  .card--back-maroon .brand__tagline { color: var(--white); }
  .card--back-maroon .brand__dot { background: var(--white); }
  .card--back-maroon .brand--centered { top: 130px; }

  .website-line {
    position: absolute; left: 0; right: 0; top: 202px;
    text-align: center; font-size: 15px; color: var(--ink);
  }
  .card--back-grey .website-line { top: 216px; }
  .card--back-grey .brand--centered { top: 136px; }

  .holder-name {
    position: absolute; right: 26px; top: 54px;
    font-size: 25px; color: var(--maroon-text); font-weight: 400;
    white-space: nowrap;
  }
  .contact {
    position: absolute; right: 26px; top: 200px;
    text-align: right; color: var(--white); font-size: 14px; line-height: 17.5px;
    list-style: none; white-space: nowrap;
  }
</style>
</head>
<body>
<main class="sheet">

  <section class="card card--front" aria-label="Card front">
    <svg class="wave" viewBox="0 0 552 312" preserveAspectRatio="none" aria-hidden="true">
      <path d="M0,222 C170,200 360,150 552,100 L552,312 L0,312 Z" fill="var(--maroon)"/>
      <path d="M0,216 C170,194 360,144 552,94" fill="none" stroke="#bdbdbd" stroke-width="1.5"/>
    </svg>
    <div class="brand brand--front">
      <div class="brand__row"><span class="brand__dot"></span><span class="brand__name">RL Advisory</span></div>
      <span class="brand__tagline">Career and Talent Pathways</span>
    </div>
    <p class="holder-name">Romy Lindqvist, MSc, PCC</p>
    <ul class="contact">
      <li>Harlow Springs, OR</li>
      <li>Phone: 503.555.0142</li>
      <li>Email: rl@romylindqvist-demo.com</li>
      <li>Twitter: @RLpathways</li>
      <li>www.romylindqvist-demo.com</li>
    </ul>
  </section>

  <section class="card card--back-white" aria-label="Card back, white">
    <div class="brand brand--centered">
      <div class="brand__row"><span class="brand__dot"></span><span class="brand__name">RL Advisory</span></div>
      <span class="brand__tagline">Career and Talent Pathways</span>
    </div>
    <p class="website-line">www.romylindqvist-demo.com</p>
  </section>

  <section class="card card--back-maroon" aria-label="Card back, maroon">
    <div class="brand brand--centered">
      <div class="brand__row"><span class="brand__dot"></span><span class="brand__name">RL Advisory</span></div>
      <span class="brand__tagline">Career and Talent Pathways</span>
    </div>
  </section>

  <section class="card card--back-grey" aria-label="Card back, grey">
    <div class="brand brand--centered">
      <div class="brand__row"><span class="brand__dot"></span><span class="brand__name">RL Advisory</span></div>
      <span class="brand__tagline">Career and Talent Pathways</span>
    </div>
    <p class="website-line">www.romylindqvist-demo.com</p>
  </section>

</main>
</body>
</html>
```